CHIP BAG AND LOGO DESIGN - A salty snack that is focused on taste and texture

I need a logo and label design for our new brand "Vantrelo". A salty snack that brings corn tortilla with extreme spices to excite the taste. First Flavor will be 'Brisa Tamarind and Salt'. Looking for a label design and a logo design for the Brand 'Vantrelo'. This brand will have multiple types of snacks and all with different flavors and heat levels.

Target Market(s)

10- 25 year old

Industry/Entity Type

Salty Snacks

Font styles to use
Sans Serif
Other font styles liked:
• Arial, Bauhaus 93, Berlin Sans FB Demi, Cooper Black

Colors
59FF00
82FF00
B8FF75
E3FFCB
F4FFEA
FFF300
FFF600
FEFA6F
FFFEC7
FFFEE8
FFC000
F8CF3A
FAE287
FDF2CF
FEFAEE
F0912C
F2A743
F7CA91
FBE8D2
FDF5EE
EE7325
F08F49
F5BC92
FAE3D3
FDF4ED
EB3D1F
EC4F4E
F09395
F8D3D4
FCEDEE

Requirements
Must have
• Colors and design that pops, need the bags to jump off the shelf in a sea of competitors. I gave an example of Puma Flax, I appreciate the artwork and design they did to differentiate their brand from others and appeal to the 10-25 demographics.
Nice to have
• Abstract / Cartoon like characteristics that speak of a south of the border recipe and origin. I would like to have in subtle grey or black background design much like the Aztec calendar that fills the space on a bag and/or a variation of that kind of design. In the front I'd like a character (maybe a warrior) of the same fashion. The logo (also being designed - "VANTRELO") carefully blended into the artwork. Bold, Loud, jumps off the shelf with bright colors and graphics.
Should not have
• bland, boring, blah colors and designs. Should be fun and loud.

```html
<!DOCTYPE html>
<html lang="en">
<head>
<meta charset="utf-8">
<title>Vantrelo – Brisa Tamarind and Salt</title>
<link rel="stylesheet" href="https://fonts.googleapis.com/css2?family=Sniglet:wght@800&family=Oswald:wght@400&display=swap">
<style>
  :root {
    --sun-yellow: #F8B922;
    --sun-gold: #EFA52A;
    --sun-pale: #F2C98A;
    --ochre: #C9A23A;
    --chili-red: #B3232A;
    --deep-red: #8E1A1F;
    --ember-orange: #EE7325;
    --flame-orange: #F0912C;
    --charcoal: #101010;
    --sky-blue: #4DA6DE;
    --jade: #2FB39A;
    --bronze: #9A4A1E;
    --paper: #FFFFFF;
    --title-shadow: #7A1418;
  }
  * { margin: 0; padding: 0; box-sizing: border-box; }
  html, body { width: 922px; height: 1200px; overflow: hidden; background: var(--sun-gold); }
  .label {
    position: relative;
    width: 922px;
    height: 1200px;
    overflow: hidden;
    background: linear-gradient(180deg, var(--sun-gold) 0%, var(--sun-yellow) 60%, var(--sun-pale) 100%);
  }
  .backdrop-pattern {
    position: absolute; inset: 0;
    background:
      linear-gradient(90deg, rgba(201,162,58,0.35) 0 4%, transparent 4% 96%, rgba(201,162,58,0.35) 96%),
      linear-gradient(135deg, rgba(240,145,44,0.3), rgba(248,207,58,0.15) 50%, rgba(201,162,58,0.35));
  }
  .tribal-block {
    position: absolute;
    left: 6px; top: 33px; width: 894px; height: 1125px;
  }
  .tribal-block svg { display: block; width: 100%; height: 100%; }
  .frame {
    position: absolute;
    left: 116px; top: 167px; width: 700px; height: 832px;
    border: 4px solid var(--paper);
  }
  .brand-badge {
    position: absolute;
    left: 356px; top: 226px; width: 211px; height: 99px;
    background: var(--paper);
    display: flex; align-items: center; justify-content: center; gap: 10px;
  }
  .brand-badge .mark { width: 10px; height: 10px; background: var(--chili-red); }
  .brand-name {
    font-family: "Oswald", sans-serif;
    font-weight: 400;
    font-size: 44px;
    line-height: 1;
    color: var(--chili-red);
  }
  .flavor-title {
    position: absolute;
    left: 116px; top: 400px; width: 700px;
    text-align: center;
    font-family: "Sniglet", sans-serif;
    font-weight: 800;
    color: var(--paper);
    font-size: 90px;
    line-height: 106px;
    text-shadow: 3px 4px 0 var(--title-shadow);
    z-index: 2;
  }
  .flavor-title span { display: block; }
  .warrior {
    position: absolute;
    top: 668px; width: 182px; height: 281px;
    background: linear-gradient(180deg, var(--jade) 0%, var(--jade) 52%, var(--bronze) 70%, var(--jade) 100%);
    border-radius: 45% 45% 18% 18%;
    z-index: 1;
  }
  .warrior.left { left: 132px; }
  .warrior.right { left: 606px; }
</style>
</head>
<body>
  <main class="label">
    <div class="backdrop-pattern" role="img" aria-label="Faint golden tribal geometric pattern background"></div>
    <div class="tribal-block" role="img" aria-label="Brush-edged panel of red, orange, black and blue tribal geometric patchwork pattern">
      <svg viewBox="0 0 894 1125" preserveAspectRatio="none" aria-hidden="true">
        <defs>
          <clipPath id="brush-edge">
            <polygon points="10,60 60,45 110,30 170,50 230,20 300,45 360,5 420,35 480,15 540,40 600,10 660,35 720,25 790,50 850,40 880,80 870,300 885,600 875,850 880,1000 860,1080 800,1060 740,1100 660,1070 580,1110 500,1080 420,1110 330,1085 250,1120 180,1090 120,1110 100,900 80,700 60,500 30,300 20,150"/>
          </clipPath>
        </defs>
        <g clip-path="url(#brush-edge)">
          <rect width="894" height="1125" fill="var(--chili-red)"/>
          <polygon points="0,0 300,0 0,300" fill="var(--charcoal)"/>
          <rect x="140" y="60" width="180" height="90" fill="var(--deep-red)"/>
          <polygon points="300,0 520,0 520,220" fill="var(--flame-orange)"/>
          <polygon points="380,70 520,130 380,190" fill="var(--sky-blue)"/>
          <rect x="600" y="0" width="294" height="380" fill="var(--charcoal)"/>
          <polygon points="520,0 640,0 640,180" fill="var(--ember-orange)"/>
          <rect x="130" y="175" width="360" height="40" fill="var(--ember-orange)"/>
          <rect x="130" y="215" width="360" height="80" fill="var(--chili-red)"/>
          <polygon points="160,255 185,230 210,255 185,280" fill="var(--sky-blue)"/>
          <polygon points="260,255 285,230 310,255 285,280" fill="var(--sky-blue)"/>
          <rect x="20" y="300" width="150" height="320" fill="var(--charcoal)"/>
          <polygon points="60,330 160,330 60,560" fill="var(--chili-red)"/>
          <polygon points="240,310 420,310 240,560" fill="var(--charcoal)"/>
          <polygon points="420,300 640,300 420,520" fill="var(--flame-orange)"/>
          <rect x="520" y="380" width="260" height="40" fill="var(--deep-red)"/>
          <polygon points="640,420 880,420 880,640" fill="var(--charcoal)"/>
          <polygon points="700,480 860,560 700,640" fill="var(--sky-blue)"/>
          <polygon points="90,620 330,620 90,860" fill="var(--flame-orange)"/>
          <polygon points="330,620 560,620 330,860" fill="var(--charcoal)"/>
          <polygon points="400,650 460,710 400,770 340,710" fill="var(--ember-orange)"/>
          <rect x="560" y="620" width="200" height="240" fill="var(--chili-red)"/>
          <polygon points="760,620 880,620 880,860" fill="var(--ember-orange)"/>
          <rect x="60" y="860" width="250" height="90" fill="var(--deep-red)"/>
          <polygon points="310,860 560,860 310,1100" fill="var(--charcoal)"/>
          <polygon points="330,950 430,950 330,1060" fill="var(--sky-blue)"/>
          <polygon points="560,860 760,860 760,1100" fill="var(--flame-orange)"/>
          <polygon points="560,900 700,1000 560,1100" fill="var(--charcoal)"/>
          <rect x="760" y="860" width="130" height="240" fill="var(--charcoal)"/>
          <rect x="120" y="960" width="190" height="160" fill="var(--ember-orange)"/>
        </g>
      </svg>
    </div>
    <div class="frame"></div>
    <div class="brand-badge">
      <span class="mark"></span>
      <span class="brand-name">VANTRELO</span>
      <span class="mark"></span>
    </div>
    <div class="warrior left" role="img" aria-label="Illustration of a feathered warrior mask in jade and bronze"></div>
    <div class="warrior right" role="img" aria-label="Illustration of a feathered warrior mask in jade and bronze"></div>
    <h1 class="flavor-title">
      <span>Brisa</span>
      <span>Tamarind</span>
      <span>and</span>
      <span>Salt</span>
    </h1>
  </main>
</body>
</html>
```